We would like to have one website and the similar (or the same) Facebook site.
We need only the first website without sub-pages and menus. We are preparing a new product for the market. On the page should be the logo, company data, few pictures and the text about our product.
The company color is red.
Company data are Tovrel GmbH, CH-7391 Uster, Switzerland, media@tovrel.com, www.tovrel.com.
Text for the page:
"We are Swiss engineers with many years of experience in ultra-precision electronics.
We develop the Kelvora, a smartwatch that can save lives. It is designed for elderly people who live alone and want to maintain their independence longer, without fear.
Our Kelvora will be available at 4th quarter of 2018."

```html
<!DOCTYPE html>
<html lang="en">
<head>
<meta charset="utf-8">
<title>Tovrel – Kelvora</title>
<link href="https://fonts.googleapis.com/css2?family=Poppins:wght@400;500;600;700&family=Open+Sans:wght@400;600&display=swap" rel="stylesheet">
<style>
:root{
  --red:#e4171f;
  --black:#111111;
  --dark:#1c1c1c;
  --dark2:#262626;
  --white:#ffffff;
  --grey:#f4f4f4;
  --text:#7a7a7a;
  --heading:#222222;
  --gold:#d9a21b;
  --line:#e3e3e3;
}
*{box-sizing:border-box;margin:0;padding:0}
html,body{width:1200px;height:4905px;overflow:hidden}
body{font-family:"Open Sans",Arial,sans-serif;color:var(--text);background:var(--white);font-size:13px;line-height:1.6}
h1,h2,h3,h4,.brand,.nav{font-family:"Poppins",Arial,sans-serif}
.wrap{width:976px;margin:0 auto;position:relative}
section,header,footer{position:relative;width:1200px}
.section-title{text-align:center;color:var(--heading);font-size:30px;font-weight:600}
.section-title::after{content:"";display:block;width:60px;height:3px;background:var(--red);margin:10px auto 0}
.ph{display:block}

/* top bar */
.topbar{height:46px;background:var(--black);color:#ddd;font-size:12px}
.topbar .wrap{display:flex;align-items:center;height:46px;gap:34px}
.topbar .item{display:flex;align-items:center;gap:8px}
.topbar .dot{width:12px;height:12px;border-radius:50%;background:var(--red)}
.topbar .social{margin-left:auto;display:flex;gap:16px}
.topbar .social span{width:10px;height:10px;border-radius:50%;background:var(--red)}

/* hero */
.hero{height:569px;background:linear-gradient(110deg,#141414 0%,#1d1d1d 45%,#2b2b2b 70%,#161616 100%);overflow:hidden}
.hero .visual{position:absolute;right:60px;top:20px;width:560px;height:540px;border-radius:40px;background:radial-gradient(ellipse at 55% 50%,#3a3a3a 0%,#262626 50%,rgba(20,20,20,0) 75%)}
.hero .nav-row{position:absolute;left:0;right:0;top:18px}
.hero .nav-row .wrap{display:flex;align-items:center;width:1150px}
.brand{color:var(--red);font-size:34px;font-weight:700;display:flex;align-items:center;gap:10px}
.brand .mark{width:14px;height:14px;background:var(--red)}
.nav{margin-left:auto;display:flex;gap:26px;font-size:11px;font-weight:600;color:var(--white);letter-spacing:.5px}
.nav .track{background:var(--red);padding:2px 8px}
.hero .copy{position:absolute;left:137px;top:140px;width:560px}
.hero h1{color:var(--white);font-size:35px;line-height:1.3;font-weight:700}
.hero h1 em{font-style:normal;color:var(--red)}
.hero p{color:#e6e6e6;font-size:13px;margin-top:30px;width:420px}
.btn{display:inline-block;background:var(--red);color:var(--white);font-family:"Poppins",Arial,sans-serif;font-size:12px;font-weight:600;padding:9px 28px;border-radius:22px;margin-top:26px}

/* about */
.about{height:660px;padding-top:78px}
.about .row{display:flex;gap:24px;margin-top:52px}
.about .photo{width:477px;height:356px;background:linear-gradient(135deg,#8a8f97 0%,#c9b7a3 55%,#6b6f77 100%)}
.about .text{flex:1;padding-top:4px}
.about .lead{color:#444;font-size:13px}
.about h3{color:var(--heading);font-size:25px;font-weight:600;margin:14px 0 16px}
.about .text p+p{margin-top:14px}

/* features */
.features{height:475px;background:linear-gradient(120deg,#1a1a1a,#2c2c2c 50%,#1a1a1a);padding-top:74px}
.features .section-title{color:var(--white)}
.features .cards{display:flex;gap:12px;margin-top:56px}
.card{width:240px;height:210px;background:var(--white);text-align:center;padding-top:40px}
.card h4{color:var(--heading);font-size:17px;font-weight:500;margin-top:14px}
.card p{font-size:12px;margin-top:8px;line-height:1.5}

/* team */
.team{height:605px;padding-top:95px}
.team .members{display:flex;gap:29px;margin-top:54px}
.member{width:222px;text-align:center}
.member .photo{height:280px;background:linear-gradient(160deg,#6f7a86 0%,#b9a590 55%,#3f4754 100%)}
.member h4{font-size:12px;color:var(--heading);font-weight:500;margin-top:16px}
.member span{font-size:12px;color:#999}

/* testimonials */
.testimonial{height:475px;padding-top:78px}
.testimonial .items{display:flex;gap:34px;margin-top:58px}
.quote{display:flex;width:470px}
.quote .photo{width:177px;height:222px;background:linear-gradient(135deg,#c7b29c,#8c7c6e 60%,#efe6dc)}
.quote .tag{width:34px;height:180px;background:var(--red);color:var(--white);font-size:11px;writing-mode:vertical-rl;text-align:center;font-weight:600}
.quote .body{flex:1;padding:0 0 0 22px;font-size:13px;color:#555;display:flex;gap:6px}
.quote .body svg{flex:none;margin-top:2px}

/* quality */
.quality{height:555px;display:flex}
.quality .left{width:600px;background:var(--dark);padding:70px 0 0 54px}
.quality h2{color:var(--white);font-size:30px;font-weight:400;line-height:1.5;width:460px}
.acc{width:490px;margin-top:30px}
.acc .head{display:flex;justify-content:space-between;align-items:center;height:40px;background:var(--white);color:var(--heading);font-size:13px;font-weight:600;padding-left:16px;margin-top:12px}
.acc .head b{width:40px;height:40px;background:var(--gold);color:var(--white);display:flex;align-items:center;justify-content:center;font-size:16px}
.acc .panel{background:var(--white);padding:12px 16px 16px;font-size:12px;border-top:1px solid var(--line)}
.acc .head.open{margin-top:0}
.quality .right{flex:1;background:linear-gradient(120deg,#d9d3cc 0%,#e8c9a8 45%,#b6875f 75%,#eae6e1 100%)}

/* blog */
.blog{height:720px;background:var(--grey);padding-top:80px}
.blog .posts{display:flex;gap:24px;margin-top:62px}
.post{width:309px;height:470px;background:var(--white)}
.post .photo{height:223px;background:radial-gradient(circle at 50% 45%,#4a4a4a 0%,#2e2e2e 45%,#222 100%)}
.post .info{padding:20px 22px}
.post .date{font-size:11px;color:#888}
.post h3{color:var(--heading);font-size:17px;font-weight:600;line-height:1.5;margin-top:10px}
.post p{font-size:12px;margin-top:10px;line-height:1.55}
.post .more{color:var(--red);font-size:12px;font-weight:600;margin-top:16px;display:block}

/* partners */
.partners{height:295px;padding-top:90px}
.partners .logos{display:flex;justify-content:space-between}
.partners .badge{width:160px;height:86px;display:flex;align-items:center;justify-content:center}
.partners .badge span{width:96px;height:44px;background:#dcdcdc;border-radius:6px}
.dots{display:flex;gap:10px;justify-content:center;margin-top:32px}
.dots span{width:7px;height:7px;border-radius:50%;background:#ccc}
.dots span:first-child{background:#666}

/* contact strip */
.strip{height:113px;background:var(--black)}
.strip .wrap{display:flex;justify-content:space-between;padding:34px 30px 0 30px;color:var(--white)}
.strip .item{display:flex;gap:14px;align-items:flex-start}
.strip strong{display:block;font-family:"Poppins",Arial,sans-serif;font-size:13px;font-weight:500}
.strip small{font-size:11px;color:#aaa}

/* footer */
.footer{height:327px;background:#1d1d1d;color:#ccc;padding-top:50px}
.footer .cols{display:flex;gap:42px}
.footer .col{width:210px}
.footer h4{color:var(--white);font-size:19px;font-weight:600;margin-bottom:12px}
.footer p{font-size:12px;line-height:1.6}
.footer ul{list-style:none;font-size:12px}
.footer li{padding:6px 0;border-bottom:1px solid #333}
.footer .contact li{border:none;display:flex;gap:10px;padding:6px 0}
.bottom{height:65px;background:#1d1d1d;border-top:1px solid #333}
.bottom .wrap{display:flex;align-items:center;height:65px}
.bottom .brand{font-size:24px}
.bottom p{margin-left:200px;color:#ccc;font-size:12px}
</style>
</head>
<body>

<div class="topbar">
  <div class="wrap" style="width:1150px">
    <div class="item"><span class="dot"></span>Seestrasse 14, CH-7391 Uster</div>
    <div class="item"><span class="dot"></span>hello@tovrel.com</div>
    <div class="item"><span class="dot"></span>+41 44 555 0192</div>
    <div class="social"><span></span><span></span><span></span><span></span><span></span></div>
  </div>
</div>

<header class="hero">
  <div class="visual ph" role="img" aria-label="Dark close-up photo of the Kelvora smartwatch on a wrist"></div>
  <div class="nav-row">
    <div class="wrap">
      <div class="brand">Tovrel</div>
      <nav class="nav">
        <span>HOME</span><span>ABOUT US</span><span>SERVICES</span><span>PROJECT</span><span>BLOG</span><span>PAGES</span><span>CONTACT US</span><span class="track">TRACK IT</span>
      </nav>
    </div>
  </div>
  <div class="copy">
    <h1>We Develop The<br>Kelvora, <em>A Smartwatch<br>That Can Save Lives</em></h1>
    <p>It is designed for elderly people who live alone and want to maintain their independence longer, without fear.</p>
    <span class="btn">READ MORE</span>
  </div>
</header>

<section class="about">
  <h2 class="section-title">About Kelvora</h2>
  <div class="wrap row">
    <div class="photo ph" role="img" aria-label="Photo of an elderly man smiling with his daughter"></div>
    <div class="text">
      <p class="lead">It is designed for elderly people who live alone and want to maintain their independence longer, without fear.</p>
      <h3>It is more than Wristwatch</h3>
      <p>We are Swiss engineers with many years of experience in ultra-precision electronics. Every part of the watch is built and tested in our own lab in Uster.</p>
      <p>We develop the Kelvora, a smartwatch that can save lives. A single touch calls for help, and falls are noticed at once, day and night.</p>
      <p>Family members stay informed through a simple app, while the wearer keeps full control over daily life at home.</p>
      <p>Our Kelvora will be available at 4th quarter of 2018. Sign up to be among the first to receive it.</p>
    </div>
  </div>
</section>

<section class="features">
  <h2 class="section-title">Features</h2>
  <div class="wrap cards">
    <div class="card">
      <svg width="30" height="26" viewBox="0 0 30 26" fill="none" stroke="#777" stroke-width="1.5"><path d="M15 24 3 12a6.5 6.5 0 0 1 12-8 6.5 6.5 0 0 1 12 8z"/></svg>
      <h4>01. Design</h4><p>Lorem ipsum dolor sit amet,<br>consectetur adipiscing elit</p>
    </div>
    <div class="card">
      <svg width="30" height="26" viewBox="0 0 30 26" fill="none" stroke="#777" stroke-width="1.5"><rect x="2" y="3" width="26" height="16"/><path d="M10 24h10M15 19v5"/></svg>
      <h4>02. Preparation</h4><p>Lorem ipsum dolor sit amet,<br>consectetur adipiscing elit</p>
    </div>
    <div class="card">
      <svg width="30" height="26" viewBox="0 0 30 26" fill="none" stroke="#777" stroke-width="1.5"><rect x="2" y="6" width="26" height="17" rx="2"/><circle cx="15" cy="14" r="5"/><path d="M10 6l2-3h6l2 3"/></svg>
      <h4>03. Construction</h4><p>Lorem ipsum dolor sit amet,<br>consectetur adipiscing elit</p>
    </div>
    <div class="card">
      <svg width="30" height="26" viewBox="0 0 30 26" fill="none" stroke="#777" stroke-width="1.5"><path d="M4 4h22v14H12l-6 5v-5H4z"/></svg>
      <h4>04. Revision</h4><p>Lorem ipsum dolor sit amet,<br>consectetur adipiscing elit</p>
    </div>
  </div>
</section>

<section class="team">
  <h2 class="section-title">Our Team</h2>
  <div class="wrap members">
    <div class="member"><div class="photo ph" role="img" aria-label="Portrait photo of a team member"></div><h4>LENA HOFER</h4><span>GARDENER</span></div>
    <div class="member"><div class="photo ph" role="img" aria-label="Portrait photo of a team member"></div><h4>LENA HOFER</h4><span>GARDENER</span></div>
    <div class="member"><div class="photo ph" role="img" aria-label="Portrait photo of a team member"></div><h4>LENA HOFER</h4><span>GARDENER</span></div>
    <div class="member"><div class="photo ph" role="img" aria-label="Portrait photo of a team member"></div><h4>LENA HOFER</h4><span>GARDENER</span></div>
  </div>
</section>

<section class="testimonial">
  <h2 class="section-title">Our Testimonial</h2>
  <div class="wrap items">
    <div class="quote">
      <div class="photo ph" role="img" aria-label="Portrait photo of a customer"></div>
      <div class="tag">Nils Berger</div>
      <div class="body">
        <svg width="14" height="12" viewBox="0 0 14 12" fill="#333"><path d="M0 12V6l3-6h3L4 6h2v6zM8 12V6l3-6h3l-2 6h2v6z"/></svg>
        <p>Lorem ipsum is simply dummy text of the printing and typesetting industry. Lorem Ipsum has been the industry's standard dummy text ever since the 1500s, when an unknown printer took a galley of type and scrambled it to make a type.</p>
      </div>
    </div>
    <div class="quote">
      <div class="photo ph" role="img" aria-label="Portrait photo of a customer"></div>
      <div class="tag">Nils Berger</div>
      <div class="body">
        <svg width="14" height="12" viewBox="0 0 14 12" fill="#333"><path d="M0 12V6l3-6h3L4 6h2v6zM8 12V6l3-6h3l-2 6h2v6z"/></svg>
        <p>Lorem ipsum is simply dummy text of the printing and typesetting industry. Lorem Ipsum has been the industry's standard dummy text ever since the 1500s, when an unknown printer took a galley of type and scrambled it to make a type.</p>
      </div>
    </div>
  </div>
</section>

<section class="quality">
  <div class="left">
    <h2>We provide high quality &amp; cost effective Kelvora</h2>
    <div class="acc">
      <div class="head open">We Are Creative &amp; Professional<b>−</b></div>
      <div class="panel">Removed demands expense account in outward tedious do. Particular way thoroughly unaffected projection favourable mrs can projecting own. Entry it matter enable becomes admire in giving.</div>
      <div class="head">Honest And Dependable<b>+</b></div>
      <div class="head">Quality Commitment<b>+</b></div>
      <div class="head">Honest And Dependable<b>+</b></div>
    </div>
  </div>
  <div class="right ph" role="img" aria-label="Photo of a smiling mother and daughter embracing"></div>
</section>

<section class="blog">
  <h2 class="section-title">Our Blog</h2>
  <div class="wrap posts">
    <article class="post"><div class="photo ph" role="img" aria-label="Product photo of the smartwatch"></div><div class="info"><div class="date">Jan, 24th 2018</div><h3>Better Nature For Better World</h3><p>Lorem Ipsum is simply dummy text of the printing and typesetting industry. Lorem Ipsum has been the industry's standard dummy text ever since the 1500s.</p><span class="more">More ›</span></div></article>
    <article class="post"><div class="photo ph" role="img" aria-label="Product photo of the smartwatch"></div><div class="info"><div class="date">Jan, 24th 2018</div><h3>Better Nature For Better World</h3><p>Lorem Ipsum is simply dummy text of the printing and typesetting industry. Lorem Ipsum has been the industry's standard dummy text ever since the 1500s.</p><span class="more">More ›</span></div></article>
    <article class="post"><div class="photo ph" role="img" aria-label="Product photo of the smartwatch"></div><div class="info"><div class="date">Jan, 24th 2018</div><h3>Better Nature For Better World</h3><p>Lorem Ipsum is simply dummy text of the printing and typesetting industry. Lorem Ipsum has been the industry's standard dummy text ever since the 1500s.</p><span class="more">More ›</span></div></article>
  </div>
</section>

<section class="partners">
  <div class="wrap logos">
    <div class="badge"><span></span></div>
    <div class="badge"><span></span></div>
    <div class="badge"><span></span></div>
    <div class="badge"><span></span></div>
    <div class="badge"><span></span></div>
  </div>
  <div class="dots"><span></span><span></span><span></span><span></span><span></span><span></span><span></span><span></span></div>
</section>

<section class="strip">
  <div class="wrap">
    <div class="item">
      <svg width="22" height="22" viewBox="0 0 24 24" fill="#fff"><path d="M6.6 10.8a15 15 0 0 0 6.6 6.6l2.2-2.2a1 1 0 0 1 1-.25 11.4 11.4 0 0 0 3.6.57 1 1 0 0 1 1 1V20a1 1 0 0 1-1 1A17 17 0 0 1 3 4a1 1 0 0 1 1-1h3.5a1 1 0 0 1 1 1c0 1.25.2 2.45.57 3.57a1 1 0 0 1-.25 1z"/></svg>
      <div><strong>+41 44 555 0100</strong><small>Monday-Friday, 8am-5pm</small></div>
    </div>
    <div class="item">
      <svg width="24" height="20" viewBox="0 0 24 20" fill="none" stroke="#fff" stroke-width="2"><rect x="1" y="2" width="22" height="16"/><path d="m1 2 11 9 11-9"/></svg>
      <div><strong>info@tovrel.com</strong><small>Drop us a line anytime</small></div>
    </div>
    <div class="item">
      <svg width="24" height="20" viewBox="0 0 24 20" fill="#fff"><path d="M2 7h5l10-6v18L7 13H2z"/></svg>
      <div><strong>Request a quote</strong><small>Get all the information</small></div>
    </div>
  </div>
</section>

<footer class="footer">
  <div class="wrap cols">
    <div class="col">
      <h4>About Us</h4>
      <p>We are Swiss engineers with many years of experience in ultra-precision electronics and safe devices.</p>
      <p style="margin-top:12px">Our Kelvora is designed for elderly people who live alone and want to stay independent longer.</p>
    </div>
    <div class="col">
      <h4>Latest Blog Post</h4>
      <ul><li>Start your own agency</li><li>How to cook down quality</li><li>Make something awesome</li><li>Plane your summer vacation</li><li>Two sunlight to enjoy</li></ul>
    </div>
    <div class="col">
      <h4>Our Project</h4>
      <ul><li>Go get an ice cream</li><li>Become the best version</li><li>Eat, Sleep and have fun</li><li>Start the pump to the top</li><li>Can you do this for us?</li></ul>
    </div>
    <div class="col">
      <h4>Contact info</h4>
      <ul class="contact">
        <li><span style="color:var(--red)">●</span>Call Us +41 44 555 0147</li>
        <li><span style="color:var(--red)">●</span>media@tovrel.com</li>
        <li><span style="color:var(--red)">●</span>Tovrel GmbH, CH-7391 Uster, Switzerland</li>
        <li><span style="color:var(--red)">●</span>Monday-Friday, 9am-6pm; Sunday Closed</li>
      </ul>
    </div>
  </div>
</footer>
<div class="bottom">
  <div class="wrap">
    <div class="brand">Tovrel</div>
    <p>All Rights Reserved · www.tovrel.com</p>
  </div>
</div>

</body>
</html>
```